Business card for medical clinic

I need an upmarket, modern medical/health business card for my clinic

Contact Information for Business Card

name, address, email, qr code

```html
<!DOCTYPE html>
<html lang="en">
<head>
<meta charset="utf-8">
<title>Meridian Care Partners – Business Card</title>
<link href="https://fonts.googleapis.com/css2?family=Montserrat:wght@400;500;700&display=swap" rel="stylesheet">
<style>
  :root {
    --bg: #e9ecef;
    --navy: #1c2a4a;
    --navy-text: #1f3a5f;
    --sky: #27a9e1;
    --mid: #2f6b92;
    --grey: #5f6670;
    --white: #ffffff;
  }
  * { box-sizing: border-box; margin: 0; padding: 0; }
  html, body {
    width: 1200px; height: 913px; overflow: hidden;
    background: var(--bg);
    font-family: "Montserrat", sans-serif;
  }
  .stage {
    position: relative; width: 1200px; height: 913px;
    display: flex; align-items: center; justify-content: center; gap: 40px;
  }
  .card {
    width: 525px; height: 300px; border-radius: 18px;
    position: relative; overflow: hidden;
    box-shadow: 0 10px 28px rgba(20, 30, 50, 0.18);
  }
  .card-front {
    background: linear-gradient(100deg, var(--navy) 0%, var(--mid) 55%, var(--sky) 100%);
    display: flex; align-items: center; justify-content: center;
  }
  .brand-name {
    font-family: "Montserrat", sans-serif;
    font-weight: 500; letter-spacing: 3px; text-transform: uppercase;
    line-height: 1.35; text-align: center;
  }
  .card-front .brand-name { color: var(--white); font-size: 26px; }
  .card-back { background: var(--white); }
  .card-back .brand {
    position: absolute; left: 30px; top: 0; bottom: 0; width: 260px;
    display: flex; align-items: center; justify-content: center;
  }
  .card-back .brand-name { color: var(--navy-text); font-size: 19px; }
  .divider {
    position: absolute; left: 305px; top: 50px; width: 1px; height: 200px;
    background: var(--sky);
  }
  .details { position: absolute; left: 325px; top: 52px; right: 20px; color: var(--grey); }
  .person-name { color: var(--navy-text); font-weight: 700; font-size: 17px; letter-spacing: 0.3px; }
  .person-title { font-size: 12px; margin-top: 2px; }
  .address { font-size: 11.5px; line-height: 1.5; margin-top: 18px; }
  .contacts { list-style: none; margin-top: 20px; font-size: 11.5px; }
  .contacts li { display: flex; align-items: center; gap: 8px; line-height: 1.7; }
  .contacts svg { width: 11px; height: 11px; flex: none; fill: var(--sky); }
</style>
</head>
<body>
<main class="stage">
  <section class="card card-front" aria-label="Card front">
    <p class="brand-name">Meridian Care<br>Partners</p>
  </section>

  <section class="card card-back" aria-label="Card back">
    <div class="brand"><p class="brand-name">Meridian Care<br>Partners</p></div>
    <div class="divider"></div>
    <div class="details">
      <p class="person-name">DANIEL MARSH</p>
      <p class="person-title">President</p>
      <p class="address">1820 Harbor View Drive<br>Seaside CA 93955</p>
      <ul class="contacts">
        <li>
          <svg viewBox="0 0 24 24" aria-hidden="true"><path d="M6.6 10.8a15.1 15.1 0 0 0 6.6 6.6l2.2-2.2a1 1 0 0 1 1-.25 11.4 11.4 0 0 0 3.6.57 1 1 0 0 1 1 1V20a1 1 0 0 1-1 1A17 17 0 0 1 3 4a1 1 0 0 1 1-1h3.5a1 1 0 0 1 1 1c0 1.25.2 2.45.57 3.6a1 1 0 0 1-.25 1z"/></svg>
          555-210-4478
        </li>
        <li>
          <svg viewBox="0 0 24 24" aria-hidden="true"><path d="M2 5h20v14H2z M2 5l10 8 10-8" /></svg>
          daniel@MeridianCare.com
        </li>
        <li>
          <svg viewBox="0 0 24 24" aria-hidden="true"><circle cx="12" cy="12" r="10"/></svg>
          www.MeridianCare.com
        </li>
      </ul>
    </div>
  </section>
</main>
</body>
</html>
```